Business Card Design Project

you do have a logo of ozul but open for anything new . main color is royal blue and white ...are give us some ideas if you like
company name is Merrow's Lawn, Tree and Landscape Contractor
PAVERS
-Pool Decks
-Driveways
-Patios
-Sidewalks & Steps
-Fire Pits
-Retaining Walls
-Layover
-All Patterns and Colors
-To view and/or create your color choice and Patterns visit www.plombastoneworks.com
Custom Concrete Work
-Sea Walls
-Slabs
-Sidewalks
-Concrete Stamping
-Custom Walls
-Custom Curbing
-Concrete Stain (Acid and Eco-Stains available)
-Concrete Sealer
-All Concrete Jobs Call And Ask
-To view and/or create your color choice visit Hargle Tint's Slab Studio app at www.slabstudioview.com
Pest Control
-Lawns insect, fungus and weed control
-Lawn Fertilization
-Outdoor Pest
- Indoor Pest Control
-Termite Control
-White Fly Treatment
-Rodent Control
IRRIGATION
-installs
-Repair
-Service of Irrigation
Landscape & Installation (residential and commercial)
-Full Lawn Care Service
-Landscape Maintenance
-Weed Control in Flower Beds
-Sod Installation
-Tree Trimming
-Tree Removal
-Bush Pruning
-All Tree & Plant Treatment for Bug, Dieses & Fungus Control
Landscape Material Delivery & Install
-Plants and Tree Install
-Rock, Mulch, Soil, Sand and Riprap
-Weed mat
-Boulders and Flagstone
-Pavers
Call 941.555.0173 for more information.
Residential, Commercial, condos, H.O.A
Lic. & Ins.

```html
<!DOCTYPE html>
<html lang="en">
<head>
<meta charset="utf-8">
<title>Merrow's Lawn, Tree and Landscape Contractor – Business Card</title>
<link rel="stylesheet" href="https://fonts.googleapis.com/css2?family=Didact+Gothic&display=swap">
<style>
  :root {
    --page-bg: #ffffff;
    --card-bg: #e9f0dc;
    --brand-green: #8db45a;
    --service-brown: #5b4433;
  }
  * { margin: 0; padding: 0; box-sizing: border-box; }
  html, body {
    width: 1200px;
    height: 763px;
    overflow: hidden;
    background: var(--page-bg);
  }
  .canvas {
    position: relative;
    width: 1200px;
    height: 763px;
    font-family: "Didact Gothic", "Century Gothic", sans-serif;
  }
  .card {
    position: absolute;
    width: 516px;
    height: 306px;
    border-radius: 22px;
    background: var(--card-bg);
    overflow: hidden;
  }
  .card--front { left: 84px; top: 76px; }
  .card--back  { left: 456px; top: 368px; }

  .brand {
    position: absolute;
    left: 72px;
    top: 86px;
    display: flex;
    align-items: center;
    gap: 18px;
    color: var(--brand-green);
  }
  .brand__mark {
    width: 92px;
    height: 92px;
    border-radius: 50%;
    background: var(--brand-green);
    flex: none;
  }
  .brand__text { display: flex; flex-direction: column; }
  .brand__name {
    font-size: 52px;
    line-height: 1;
    letter-spacing: 2px;
    text-transform: uppercase;
  }
  .brand__tagline {
    margin-top: 8px;
    font-size: 13px;
    letter-spacing: 1px;
    text-transform: uppercase;
  }

  .services {
    position: absolute;
    left: 0;
    right: 0;
    top: 46px;
    list-style: none;
    text-align: center;
    color: var(--service-brown);
    font-size: 19px;
    line-height: 28px;
    text-transform: uppercase;
  }
  .contact {
    position: absolute;
    left: 0;
    right: 0;
    top: 250px;
    text-align: center;
    color: var(--service-brown);
    font-size: 19px;
    text-transform: uppercase;
  }
</style>
</head>
<body>
<main class="canvas">
  <section class="card card--front" aria-label="Card front">
    <div class="brand">
      <span class="brand__mark" aria-hidden="true"></span>
      <div class="brand__text">
        <span class="brand__name">Merrow's</span>
        <span class="brand__tagline">Lawn, Tree &amp; Landscape Contractor</span>
      </div>
    </div>
  </section>

  <section class="card card--back" aria-label="Card back">
    <ul class="services">
      <li>Pavers</li>
      <li>Custom Concrete Work</li>
      <li>Pest Control</li>
      <li>Irrigation</li>
      <li>Landscape &amp; Installation</li>
      <li>Landscape Material Delivery &amp; Install</li>
    </ul>
    <p class="contact">Call 941.555.0173 for more information</p>
  </section>
</main>
</body>
</html>
```